A1 Poster Design for ecig vendor in a shopping mall

I need an A1 poster designing for an ecig outlet in a shopping mall. i have included graphics that i would like to be displayed. I would like the message to convey the following:

The finest british made eliquids. buy 3 10ml bottles for only £10
Vaping kits, Mods & accessories
Genuine products from Veltro, Dulvo, Morpivex, Barudel
Plume-Mist Vaping

Industry/Entity Type

Shopping

Font styles to use
Serif
Sans Serif
Script

```html
<!DOCTYPE html>
<html lang="en">
<head>
<meta charset="utf-8">
<title>Plume-Mist Vaping – Poster</title>
<link rel="stylesheet" href="https://fonts.googleapis.com/css2?family=Pinyon+Script&family=Cormorant+Garamond:wght@500;600&family=Montserrat:wght@400;500&display=swap">
<style>
  :root {
    --ink: #050505;
    --ink-soft: #1b1b1d;
    --grey-base: #8d8f93;
    --white: #f4f4f4;
    --sky: #7fd3ef;
    --smoke: #5a5d63;
    --fruit: #b3452c;
    --badge-red: #c8262b;
    --badge-blue: #2a4a8f;
    --badge-pink: #d58a9a;
    --badge-green: #2f8a3c;
  }
  * { margin: 0; padding: 0; box-sizing: border-box; }
  html, body { width: 841px; height: 1200px; overflow: hidden; background: var(--ink); }
  .poster {
    position: relative;
    width: 841px;
    height: 1200px;
    background: linear-gradient(180deg, var(--ink) 0%, var(--ink) 62%, var(--ink-soft) 80%, var(--grey-base) 100%);
    color: var(--white);
    font-family: "Cormorant Garamond", Georgia, serif;
  }
  .hero-art {
    position: absolute;
    left: 60px; top: 20px;
    width: 250px; height: 1080px;
    background:
      radial-gradient(ellipse at 50% 30%, rgba(179,69,44,0.55) 0%, rgba(179,69,44,0) 40%),
      radial-gradient(ellipse at 50% 55%, rgba(200,200,205,0.35) 0%, rgba(90,93,99,0) 60%),
      linear-gradient(180deg, rgba(90,93,99,0.5) 0%, rgba(30,30,32,0.6) 70%, rgba(20,20,22,0.2) 100%);
    border-radius: 40px;
  }
  .brand {
    position: absolute;
    left: 500px; top: 38px;
    width: 260px;
    text-align: center;
  }
  .brand-name {
    font-size: 56px; font-weight: 600; letter-spacing: 4px;
    color: var(--white); line-height: 1;
  }
  .brand-tag {
    font-family: "Montserrat", Arial, sans-serif;
    font-size: 12px; letter-spacing: 2px; color: var(--sky);
    margin-top: 6px;
  }
  .content {
    position: absolute;
    left: 330px; width: 480px; top: 150px;
    text-align: center;
  }
  .headline {
    font-family: "Pinyon Script", cursive;
    font-size: 54px; line-height: 58px; color: var(--white);
  }
  .divider {
    width: 130px; height: 1px; background: var(--white);
    margin: 24px auto; opacity: 0.7;
  }
  .offer {
    font-size: 78px; font-weight: 500; line-height: 84px;
    color: var(--sky);
  }
  .range {
    font-family: "Montserrat", Arial, sans-serif;
    font-size: 17px; letter-spacing: 3px; margin-top: 78px;
  }
  .genuine {
    font-family: "Montserrat", Arial, sans-serif;
    font-size: 22px; color: var(--sky); margin-top: 24px; line-height: 32px;
  }
  .rule {
    width: 340px; height: 1px; background: var(--white); opacity: 0.5;
    margin: 26px auto 22px;
  }
  .shop-name { font-size: 34px; font-weight: 500; color: var(--white); }
  .badges {
    position: absolute; left: 340px; top: 1050px;
    display: flex; gap: 28px; align-items: center;
  }
</style>
</head>
<body>
<main class="poster">
  <div class="hero-art" role="img" aria-label="Vape pen at the bottom with a rising trail of smoke carrying chocolate, apple, melon and strawberry pieces"></div>

  <header class="brand">
    <div class="brand-name">NIMBRA</div>
    <div class="brand-tag">PLUME-MIST VAPING</div>
  </header>

  <section class="content">
    <h1 class="headline">The finest<br>british made<br>eliquids</h1>
    <div class="divider"></div>
    <p class="offer">Buy 3<br>10ml bottles<br>for only £10</p>
    <div class="divider"></div>
    <p class="range">VAPING KITS • MODS • ACCESSORIES</p>
    <p class="genuine">Genuine products from<br>Veltro, Dulvo, Morpivex, Barudel</p>
    <div class="rule"></div>
    <p class="shop-name">Plume-Mist Vaping</p>
  </section>

  <svg class="badges" width="240" height="50" viewBox="0 0 240 50" aria-hidden="true">
    <circle cx="22" cy="25" r="20" fill="var(--badge-red)"/>
    <rect x="58" y="8" width="50" height="34" fill="var(--badge-blue)"/>
    <circle cx="150" cy="25" r="20" fill="var(--badge-pink)"/>
    <rect x="186" y="6" width="46" height="38" fill="var(--badge-green)"/>
  </svg>
</main>
</body>
</html>
```